Brantley Water Taxi and Transport

Need to redesign our business cards to relay that we do freight logistics and water taxi service. We also work with gov. agencies doing environmental clean up, oil spill response, remote site construction and work with many of the air taxi and helicopter services on Kodiak Island. Out website is www.brantleywatertaxi-example.com to get a better idea of what we do.

Contact Information for Business Card

I have a previous business card but it just has the logo on the front, and a sunset picture on the back with the contact info. It does not relay what we do and what we can help with. I like a simple straight forward design over a busy one.

Colors
3176b5
0455a3
cfdfed

Requirements
Must have
• logo, email, website, phone number

```html
<!DOCTYPE html>
<html lang="en">
<head>
<meta charset="utf-8">
<title>Brantley Water Taxi and Transport – Business Card</title>
<link href="https://fonts.googleapis.com/css2?family=Raleway:wght@400;500;600&display=swap" rel="stylesheet">
<style>
  :root {
    --backdrop: #444547;
    --card: #f2f2f2;
    --brand-blue: #1f45a5;
    --sky-blue: #4ab0d9;
    --ink: #3c3c3c;
    --white: #ffffff;
  }
  * { margin: 0; padding: 0; box-sizing: border-box; }
  html, body { width: 1200px; height: 900px; overflow: hidden; }
  body {
    background: var(--backdrop);
    font-family: "Raleway", sans-serif;
    position: relative;
  }
  .card {
    position: absolute;
    left: 336px;
    width: 526px;
    height: 300px;
    background: var(--card);
    overflow: hidden;
  }
  .card--front { top: 116px; }
  .card--back { top: 471px; }

  /* Front */
  .brand-name {
    position: absolute;
    right: 24px;
    top: 30px;
    text-align: right;
    color: var(--brand-blue);
    font-weight: 600;
    font-size: 19px;
    line-height: 1.25;
  }
  .phone {
    position: absolute;
    right: 24px;
    top: 78px;
    font-size: 16px;
    color: var(--ink);
    letter-spacing: 0.2px;
  }
  .contact-band {
    position: absolute;
    left: 0;
    top: 134px;
    width: 526px;
    height: 26px;
  }
  .contact-band__text {
    position: absolute;
    right: 18px;
    top: 3px;
    font-size: 17px;
    color: var(--white);
    white-space: nowrap;
  }
  .services {
    position: absolute;
    left: 22px;
    top: 194px;
    list-style: none;
    color: var(--ink);
    font-size: 17px;
    line-height: 22.7px;
  }
  .services li { position: relative; padding-left: 16px; }
  .services li::before {
    content: "";
    position: absolute;
    left: 0;
    top: 9px;
    width: 5px;
    height: 5px;
    background: var(--brand-blue);
  }

  /* Back */
  .brand-mark {
    position: absolute;
    left: 50%;
    top: 58px;
    transform: translateX(-50%);
    width: 64px;
    height: 64px;
    border-radius: 50%;
    background: var(--sky-blue);
  }
  .brand-lockup {
    position: absolute;
    left: 0;
    right: 0;
    top: 138px;
    text-align: center;
    color: var(--brand-blue);
    font-weight: 600;
    font-size: 26px;
    line-height: 1.2;
  }
  .web-band {
    position: absolute;
    left: 0;
    top: 255px;
    width: 526px;
    height: 26px;
  }
  .web-band__text {
    position: absolute;
    left: 35px;
    top: 3px;
    font-size: 17px;
    color: var(--white);
    white-space: nowrap;
  }
</style>
</head>
<body>

<section class="card card--front" aria-label="Card front">
  <div class="brand-name">Brantley<br>Water Taxi &amp; Transport</div>
  <div class="phone">021/555.01.234</div>

  <div class="contact-band">
    <svg width="526" height="26" viewBox="0 0 526 26" aria-hidden="true">
      <polygon points="100,0 114,0 132,26 118,26" fill="var(--sky-blue)"/>
      <polygon points="124,0 138,0 156,26 142,26" fill="var(--brand-blue)"/>
      <polygon points="148,0 162,0 180,26 166,26" fill="var(--brand-blue)"/>
      <polygon points="172,0 526,0 526,26 190,26" fill="var(--brand-blue)"/>
    </svg>
    <span class="contact-band__text">your.email@brantley-example.com</span>
  </div>

  <ul class="services">
    <li>Freight logistics</li>
    <li>Water taxi service</li>
    <li>Environmental clean up</li>
    <li>Oil spill response</li>
  </ul>
</section>

<section class="card card--back" aria-label="Card back">
  <div class="brand-mark" aria-hidden="true"></div>
  <div class="brand-lockup">Brantley<br>Water Taxi &amp; Transport</div>

  <div class="web-band">
    <svg width="526" height="26" viewBox="0 0 526 26" aria-hidden="true">
      <polygon points="0,0 364,0 346,26 0,26" fill="var(--brand-blue)"/>
      <polygon points="380,0 394,0 376,26 362,26" fill="var(--brand-blue)"/>
      <polygon points="404,0 418,0 400,26 386,26" fill="var(--brand-blue)"/>
      <polygon points="428,0 442,0 424,26 410,26" fill="var(--sky-blue)"/>
    </svg>
    <span class="web-band__text">www.brantleywatertaxi-example.com</span>
  </div>
</section>

</body>
</html>
```